Business Consultancy Wordpress Design

Small business analysis consultancy.

Looking for a bold, clean design for Wordpress. Final site will only be a few pages, some contact information, services provided and a little background information. Potentially a blog.

Colours to be as per logo, with either black or white as the main colour.

Link is www.brevikadvisory.com

More details to be included in the best few days

Name - Brevik Advisory
Provides - Project Consultancy
Updates

Project Deadline Extended
Reason: I am going to be on holiday with little access to the web over 28/02 - 05/03 and am therefore extending the deadline

Target Market(s)

Business professionals

Industry/Entity Type

Business

Colors

Designer to choose colors to be used in the design.

Requirements
Must have
• Must contain the logo in the header
Footer must fit a 3 column layout in wordpress

Business style, royalty free stock images
Nice to have
• Would like the 1 or 2 column wordpress style layout
Should not have
• must not be blog or magazine style layout or look and feel

```html
<!DOCTYPE html>
<html lang="en">
<head>
<meta charset="utf-8">
<title>Brevik Advisory</title>
<link href="https://fonts.googleapis.com/css2?family=Michroma&family=Open+Sans:wght@400;600&display=swap" rel="stylesheet">
<style>
:root{
  --blue:#1a8fd0;
  --blue-dark:#0d77b7;
  --blue-light:#33aee6;
  --green:#5ba63a;
  --green-dark:#3f8a24;
  --ink:#2d2d2d;
  --text:#666;
  --grey-line:#d6d8dc;
  --services-bg:#eeeeef;
  --about-bg:#f4f6fa;
  --footer-bg:#e2e5ee;
  --white:#fff;
}
*{box-sizing:border-box;margin:0;padding:0}
html,body{width:774px;height:1200px;overflow:hidden}
body{position:relative;background:var(--white);font-family:"Open Sans",Arial,sans-serif;color:var(--text)}
.abs{position:absolute}
.display{font-family:"Michroma","Arial Black",sans-serif;text-transform:uppercase}

.top-strip{left:0;top:0;width:774px;height:5px;background:#e4e4e6}
.site-header{left:0;top:5px;width:774px;height:71px;background:var(--white)}
.brand{left:46px;top:31px;display:flex;align-items:center;gap:8px}
.brand-dot{width:22px;height:22px;border-radius:50%;background:var(--blue)}
.brand-name{font-size:15px;color:#666;letter-spacing:.2px;text-transform:uppercase}
.social-top{left:656px;top:25px;display:flex;gap:6px}
.social-top span{width:18px;height:18px;border-radius:50%;background:var(--blue)}
.phone{left:598px;top:51px;display:flex;align-items:center;gap:6px;font-size:13px;color:#555;letter-spacing:1px}

.main-nav{left:0;top:76px;width:774px;height:36px;background:linear-gradient(#2ea7e2,var(--blue-dark))}
.main-nav a{position:absolute;top:0;height:36px;line-height:36px;color:var(--white);font-size:8.5px;letter-spacing:1px;text-decoration:none;font-family:"Michroma",sans-serif}
.main-nav .active{background:#167fc0;padding:0 5px}
.search{left:598px;top:82px;width:136px;height:21px;background:var(--white);border-radius:2px;font-size:8px;color:#999;padding:5px 6px}

.hero{left:0;top:112px;width:774px;height:238px;background:linear-gradient(180deg,#b9d8ef 0%,#6e8aa3 35%,#2a3440 60%,#98b7cf 85%,#eaf3fa 100%)}

.services{left:0;top:350px;width:774px;height:296px;background:var(--services-bg)}
.section-title{width:774px;text-align:center;font-size:13.5px;letter-spacing:1.5px;color:var(--blue)}
.section-title em{font-style:normal;color:var(--green)}
.divider{left:46px;width:672px;height:1px;background:var(--grey-line)}
.divider-dot{left:381px;width:11px;height:11px;border-radius:50%;background:var(--blue)}
.service{width:200px;text-align:center}
.service h3{font-size:8.5px;color:var(--ink);letter-spacing:1px;margin-top:10px;font-weight:400}
.service p{font-size:10px;line-height:13.6px;letter-spacing:.6px;margin-top:6px}
.read-more{font-size:8px;color:var(--blue);letter-spacing:1px;text-transform:uppercase;margin-top:5px;display:block}
.btn-green{left:340px;top:594px;width:103px;height:21px;background:linear-gradient(#62b040,var(--green-dark));color:var(--white);font-size:8.5px;letter-spacing:.8px;text-align:center;line-height:21px;border-radius:2px}

.about{left:0;top:646px;width:774px;height:370px;background:var(--about-bg)}
.portrait{left:118px;top:708px;width:128px;height:145px;background:#dcdde0;padding:4px}
.portrait div{width:100%;height:100%;background:linear-gradient(180deg,#f4f4f4 0%,#c9ccd0 50%,#2c2f36 100%)}
.about-copy{left:273px;top:727px;width:410px;font-size:10px;line-height:13.6px;letter-spacing:.6px}
.about-copy p+p{margin-top:13px}

.newsletter{left:130px;top:914px;width:539px;height:64px;background:linear-gradient(90deg,var(--blue-dark),var(--blue-light) 60%,var(--blue-dark));border:1px solid #0b6aa5}
.newsletter-inner{left:136px;top:920px;width:527px;height:52px;border:1px solid rgba(255,255,255,.35)}
.mailbox{left:142px;top:886px;width:58px;height:78px;background:linear-gradient(#3aa0e0,#0e5fa0);border-radius:22px 22px 4px 4px}
.nl-label{left:213px;top:924px;font-size:8px;color:var(--white);letter-spacing:1px;font-family:"Michroma",sans-serif}
.nl-input{left:213px;top:939px;width:337px;height:23px;background:var(--white);font-size:10px;color:#999;padding:5px 13px;letter-spacing:1px}
.nl-btn{left:562px;top:939px;width:86px;height:23px;background:linear-gradient(#6ab84a,var(--green-dark));color:var(--white);font-size:9px;line-height:23px;text-align:center;letter-spacing:1px;font-family:"Michroma",sans-serif}

.site-footer{left:0;top:1016px;width:774px;height:154px;background:var(--footer-bg)}
.footer-heading{font-size:9.5px;color:var(--blue);letter-spacing:1.2px}
.footer-rule{height:1px;background:#c7cad3}
.blog-thumb{left:44px;top:1077px;width:102px;height:70px;background:#222;padding:4px}
.blog-thumb div{width:100%;height:100%;background:linear-gradient(180deg,#f0f2f5,#a8b3c0)}
.blog-text{left:152px;top:1076px;width:160px;font-size:9px;line-height:11px;letter-spacing:.4px}
.blog-text h4{font-weight:400;font-size:10px;color:#555;letter-spacing:1px;margin-bottom:1px}
.blog-text a{color:var(--blue);display:block;margin-top:6px;text-decoration:none}
.touch-row{left:349px;display:flex;align-items:center;gap:6px;font-size:10px;color:#555;letter-spacing:.8px}
.touch-row span{width:17px;height:17px;border-radius:50%;background:var(--blue)}
.quick{font-size:10px;color:#555;letter-spacing:.8px}
.quick b{color:var(--blue);margin-right:3px}
.bottom-bar{left:0;top:1170px;width:774px;height:30px;background:var(--blue);color:var(--white);font-size:6px;line-height:30px;text-align:center;letter-spacing:.8px;font-family:"Michroma",sans-serif}
</style>
</head>
<body>
<div class="abs top-strip"></div>
<header class="abs site-header"></header>
<div class="abs brand"><span class="brand-dot"></span><span class="brand-name">Brevik Advisory</span></div>
<div class="abs social-top"><span></span><span></span><span></span></div>
<div class="abs phone">
  <svg width="12" height="12" viewBox="0 0 12 12"><rect width="12" height="12" rx="2" fill="#1a8fd0"/><path d="M4 3c-1 1 0 3 2 5s3 2.5 4 1.5l-1-1.2-1 .5C7 8 5 6 4.9 5.2l.6-.9L4 3z" fill="#fff"/></svg>
  02-5550-1947
</div>

<nav class="abs main-nav">
  <a class="active" style="left:46px">HOME</a>
  <a style="left:126px">ABOUT</a>
  <a style="left:210px">SERVICES</a>
  <a style="left:313px">BLOG</a>
  <a style="left:387px">CONTACT</a>
</nav>
<div class="abs search">Keyword Search...
  <svg class="abs" style="right:5px;top:4px" width="13" height="13" viewBox="0 0 13 13"><circle cx="5" cy="5" r="3.5" fill="none" stroke="#aaa" stroke-width="1.6"/><path d="M7.5 7.5l4 4" stroke="#aaa" stroke-width="2"/></svg>
</div>

<div class="abs hero" role="img" aria-label="Photo of business people meeting in silhouette before a bright office window"></div>

<section class="abs services"></section>
<h2 class="abs section-title display" style="top:378px">Services <em>Offered</em></h2>
<div class="abs divider" style="top:404px"></div>
<div class="abs divider-dot" style="top:399px"></div>

<div class="abs service" style="left:82px;top:448px">
  <svg width="48" height="34" viewBox="0 0 48 34"><rect x="12" y="2" width="8" height="10" rx="2" fill="#2d2d2d"/><rect x="28" y="2" width="8" height="10" rx="2" fill="#2d2d2d"/><circle cx="12" cy="22" r="11" fill="#2d2d2d"/><circle cx="36" cy="22" r="11" fill="#2d2d2d"/><rect x="18" y="12" width="12" height="10" fill="#2d2d2d"/><circle cx="12" cy="23" r="6" fill="#fff"/><circle cx="36" cy="23" r="6" fill="#fff"/><circle cx="12" cy="23" r="4" fill="#1a8fd0"/><circle cx="36" cy="23" r="4" fill="#1a8fd0"/></svg>
  <h3 class="display">Project Scoping</h3>
  <p>Lorem ipsum dolor sit amet, consectetur adipiscing elit. Ut felis ligula, dignissim sit amet</p>
  <span class="read-more">Read more ›</span>
</div>
<div class="abs service" style="left:287px;top:448px">
  <svg width="42" height="34" viewBox="0 0 42 34"><rect x="14" y="0" width="14" height="7" rx="2" fill="none" stroke="#2d2d2d" stroke-width="3"/><rect x="1" y="6" width="40" height="28" rx="3" fill="#2d2d2d"/><rect x="5" y="14" width="32" height="7" fill="#1a8fd0"/><rect x="9" y="12" width="5" height="11" fill="#fff"/><rect x="28" y="12" width="5" height="11" fill="#fff"/></svg>
  <h3 class="display">Methods &amp; Approach</h3>
  <p>Lorem ipsum dolor sit amet, consectetur adipiscing elit. Ut felis ligula, dignissim sit amet</p>
  <span class="read-more">Read more ›</span>
</div>
<div class="abs service" style="left:500px;top:448px">
  <svg width="40" height="34" viewBox="0 0 40 34"><ellipse cx="16" cy="5" rx="13" ry="4" fill="#2d2d2d"/><rect x="3" y="7" width="26" height="7" rx="3" fill="#2d2d2d"/><rect x="3" y="16" width="26" height="7" rx="3" fill="#2d2d2d"/><rect x="3" y="25" width="20" height="7" rx="3" fill="#2d2d2d"/><path d="M27 18h5v6h6v5h-6v5h-5v-5h-6v-5h6z" fill="#1a8fd0"/></svg>
  <h3 class="display">Issue &amp; Risk Management</h3>
  <p>Lorem ipsum dolor sit amet, consectetur adipiscing elit. Ut felis ligula, dignissim sit amet</p>
  <span class="read-more">Read more ›</span>
</div>
<div class="abs btn-green">View our services</div>

<section class="abs about"></section>
<h2 class="abs section-title display" style="top:664px">About <em>Brevik</em></h2>
<div class="abs divider" style="top:692px"></div>
<div class="abs divider-dot" style="top:687px"></div>
<div class="abs portrait"><div role="img" aria-label="Portrait photo of the firm's principal consultant in a dark suit"></div></div>
<div class="abs about-copy">
  <p>Lorem ipsum dolor sit amet, consectetur adipiscing elit. Ut felis ligula, dignissim sit amet interdum non, lobortis eget lacus. Nulla ultricies at eros non auctor. Donec elementum ante vel eros tempus blandit. Phasellus condimentum mollis pellentesque.</p>
  <p>Nulla ultricies at eros non auctor. Donec elementum ante vel eros tempus blandit. Phasellus condimentum mollis pellentesque.</p>
  <span class="read-more">Read more ›</span>
</div>

<div class="abs newsletter"></div>
<div class="abs newsletter-inner"></div>
<div class="abs mailbox" role="img" aria-label="Illustration of a blue mailbox"></div>
<div class="abs nl-label">JOIN TO OUR NEWSLETTER</div>
<div class="abs nl-input">Email address</div>
<div class="abs nl-btn">JOIN NOW!</div>

<footer class="abs site-footer"></footer>
<h3 class="abs footer-heading display" style="left:43px;top:1043px">From our blog</h3>
<div class="abs footer-rule" style="left:42px;top:1064px;width:250px"></div>
<div class="abs blog-thumb"><div role="img" aria-label="Photo of a presenter pointing at a growth chart"></div></div>
<div class="abs blog-text">
  <h4>BLOG TITLE GOES HERE</h4>
  Lorem ipsum dolor sit amet, consectetur adipiscing elit consectetur adipiscing elitconsectetur adipiscing elit adipiscing
  <a>more &gt;&gt;</a>
</div>
<h3 class="abs footer-heading display" style="left:342px;top:1043px">Keep in touch</h3>
<div class="abs footer-rule" style="left:336px;top:1064px;width:165px"></div>
<div class="abs touch-row" style="top:1074px"><span></span>Our chirpline page</div>
<div class="abs touch-row" style="top:1097px"><span></span>Our friendbook page</div>
<div class="abs touch-row" style="top:1120px"><span></span>Our Worknet page</div>
<h3 class="abs footer-heading display" style="left:588px;top:1043px">Quicklinks</h3>
<div class="abs footer-rule" style="left:580px;top:1064px;width:167px"></div>
<div class="abs quick" style="left:586px;top:1075px"><b>›</b>Home</div>
<div class="abs quick" style="left:658px;top:1075px"><b>›</b>Blog</div>
<div class="abs quick" style="left:586px;top:1098px"><b>›</b>About</div>
<div class="abs quick" style="left:658px;top:1098px"><b>›</b>Contact</div>
<div class="abs quick" style="left:586px;top:1121px"><b>›</b>Services</div>
<div class="abs bottom-bar">COPYRIGHT © 2014 BREVIK ADVISORY</div>
</body>
</html>
```